Podcast covert art for startup show

I need podcast cover art that stands out and clearly says what the podcast is about: startup stories.

This is an example of Castrova cover art:
https://www.filebarnex.com/s/q4k8tmwpl2vbx9r/Castrova%202.png?dl=0

You can see how mine is looking blah on this page:
https://www.filebarnex.com/s/7h3jrdkqa5wzm2f/My%20podcast%20art%20doesn%27t%20stand%20out%20enough.png?dl=0

I need something that will get attention on a page that's full of other podcast covers and be easy to read.

SOMETHINGS THAT MIGHT HELP:

I love how easy it is to read the titles of these podcasts:
https://www.filebarnex.com/s/wpx6ghtmr0cqv84/easy%20to%20read%20titles.png?dl=0

I love how the logos of these podcasts are easy to read but they don't take much space:
https://www.filebarnex.com/s/5t2yfnbkd8jxe63/nice%20logo%20placement.png?dl=0

Target Market(s)

Successful software entrepreneurs

Industry/Entity Type

Startup

Font styles to use
Serif

Colors
00a990

Requirements
Must have
• I need it to include this:
• - This phrase: Startup Stories
• - My logo (keep it small, but readable)
• - My photo
• MY LOGO:
• http://talvoren.com/logo
• MY FAVORITE PHOTO OF MYSELF:
• https://vault.stormlake.net/open?id=0Xq7T_pwkr5bnHYmQZAaLPKKRw3
• You can edit my photo any way you want, including removing the background, turning me into a black&white photo, etc
• OTHER PHOTOS OF ME:
• https://vault.stormlake.net/open?id=0Xq7T_pwkr5bnW8JdvqXAcMbPZN
• Castrova asks that the size be 3000 x 3000 pixels
Nice to have
• I prefer that it have have 1 dominating color to help it stand out.
• This is what I mean:
• https://www.filebarnex.com/s/q4k8tmwpl2vbx9r/Castrova%20-%20one%20dominating%20color.png?dl=0
• I really like this color:
• https://www.filebarnex.com/s/k9v1wfzhr3ndy7c/color%20I%20like.png?dl=0

```html
<!DOCTYPE html>
<html lang="en">
<head>
<meta charset="utf-8">
<title>Talvoren — Startup Stories podcast cover</title>
<link rel="stylesheet" href="https://fonts.googleapis.com/css2?family=Montserrat:wght@500;700&display=swap">
<style>
  :root {
    --green-deep: #2d6a56;
    --green-light: #3a9479;
    --green-mid: #33806a;
    --band-white: #f1f1ef;
    --title-green: #2c6b57;
    --logo-gold: #f3c646;
    --photo-light: #b9b9b9;
    --photo-dark: #3e3e3e;
  }
  html, body {
    margin: 0;
    padding: 0;
    overflow: hidden;
    background: #ffffff;
  }
  .cover {
    position: relative;
    width: 1200px;
    height: 1200px;
    overflow: hidden;
    background: var(--green-deep);
    font-family: "Montserrat", Arial, sans-serif;
  }
  .cover__shapes {
    position: absolute;
    inset: 0;
  }
  .host-photo {
    position: absolute;
    left: 360px;
    top: 70px;
    width: 760px;
    height: 740px;
    background: radial-gradient(ellipse at 40% 35%, var(--photo-light) 0%, #8a8a8a 40%, var(--photo-dark) 100%);
    opacity: 0.92;
    clip-path: polygon(18% 0, 70% 0, 100% 40%, 100% 100%, 0 100%, 6% 40%);
  }
  .brand {
    position: absolute;
    left: 50px;
    top: 34px;
    margin: 0;
    font-weight: 700;
    font-size: 76px;
    letter-spacing: 2px;
    line-height: 1;
    color: var(--logo-gold);
  }
  .title-band {
    position: absolute;
    right: 0;
    height: 156px;
    background: var(--band-white);
    display: flex;
    align-items: center;
  }
  .title-band--top { left: 228px; top: 768px; }
  .title-band--bottom { left: 300px; top: 972px; }
  .title-band__text {
    margin: 0;
    padding-left: 48px;
    font-weight: 500;
    font-size: 136px;
    letter-spacing: 6px;
    line-height: 1;
    color: var(--title-green);
  }
  .title-band--bottom .title-band__text { padding-left: 24px; }
</style>
</head>
<body>
  <main class="cover">
    <svg class="cover__shapes" width="1200" height="1200" viewBox="0 0 1200 1200" aria-hidden="true">
      <polygon points="0,642 1200,516 1200,1200 0,1200" fill="var(--green-light)"/>
      <polygon points="300,1128 1200,1060 1200,1200 380,1200" fill="var(--green-deep)"/>
      <polygon points="300,1128 1200,1128 1200,1068" fill="var(--band-white)"/>
    </svg>

    <div class="host-photo" role="img" aria-label="Black-and-white photo of the podcast host smiling with his fist extended toward the viewer"></div>

    <p class="brand">TALVOREN</p>

    <div class="title-band title-band--top">
      <h1 class="title-band__text">STARTUP</h1>
    </div>
    <div class="title-band title-band--bottom">
      <p class="title-band__text">STORIES</p>
    </div>
  </main>
</body>
</html>
```